Web-page design

We need a initial web design for our page kelbrook.com.au (which is not yet set up).
We provide consulting services for all kinds of problems in and between organisations.
Main focus is on conflict resolution but we also support companies on improving their operational performance.
We want to have the following page structure (and part of the project is to design the 8 pages):
- Home
- Services (we offer 3 main service areas - one per page)
- Case studies (one per page)
- Engaging us (our process)
- About Conflict & low performance
- Conflict resolution App
- About
- Contact (Email form)
- Our logo should be on each page.
The start page should include the following information:
- Twitter / Linkedin / facebook/ google + Links
- Telephone / Email or in general contact details
- News
- A quite prominent picture box with 3 alternating pics - each representing one of our service areas
- Link to our App
- Testimonials
It would be nice if the service pages would have an image header. Links to the information section (about conflict & low performance; and the app page) would be nice as well.
We like the following joomla designs: www.frandelthemes.com/itempreview/153
No need to copy it, it should just give you an idea.
We like the layout here with the picture and space for the case studies on the left. Somewhere beneath should be the 3 service areas with a picture each.
In terms of colors: our logo colours are Blue (RBG 8;44;80) and Orange (RGB 231;120;23). The orange could be used to emphasise certain things, however there should not be too much color.
Budget for images available, so please use placeholders or ask us for specific photos/images, if you need them for your design.
Updates
Hi, one more thing that we would like to have is the case studies not hidden behind a link "case studies" - we would like to have them individually linked prominent on the first page. There will be about 6-8 of them. Thats what we liked on the joomla template (the links left from the picture).
Hi, thanks very much for all the great proposals.
We are currently going through the selection process and will post our decision early next week.
Thanks again!
Wilma
Target Market(s)
- target customers are all different kinds of businesses and organisations (all industries, government, non-for-profit, ...) experiencing conflict and tension - be it with internal staff, amongst managers or board members, dysfunctional teams, between organizations or customers and organizations... examples could be bullying allegations, governmental negotiations with unions, disputes within organizations etc.
- also we will offer performance improvement services for organizations
- we will offer mediation, facilitation, negotiation, performance improvement services, conflict coaching, conflict management, change management services
- if comparable to anything - then to a law firm in terms of dealing with conflicts but its much less adversarial and much more about the people and their interests rather than about laws
- basically it's all kind of things you can do in order to solve disputes without involving lawyers and a court - so it's much cheaper and target is to find a solution all parties can live with rather than having a judge deciding about who wins and who looses
- performance management is more about analysing reasons for a lack of performance and setting up continous improvement systems, supporting change management, facilitating improvement workshops or strategic meetings, ...
Industry/Entity Type
Consulting
Look and feel

```html
<!DOCTYPE html>
<html lang="en">
<head>
<meta charset="utf-8">
<title>Harrow Lindqvist – Conflict Resolution &amp; Performance</title>
<link href="https://fonts.googleapis.com/css2?family=Arimo:wght@400;700&family=Roboto:wght@300;400;500&family=Roboto+Condensed:wght@700&display=swap" rel="stylesheet">
<style>
:root{
  --navy:#082c50;
  --orange:#e77817;
  --page-bg:#ececec;
  --panel:#f7f7f7;
  --dark:#2b2b2b;
  --nav:#2e2e2e;
  --text:#3a3a3a;
  --muted:#8a8a8a;
  --rule:#bdbdbd;
}
*{box-sizing:border-box;margin:0;padding:0}
html,body{width:1198px;height:1200px;overflow:hidden}
body{background:var(--page-bg);font-family:"Arimo",Arial,sans-serif;color:var(--text);position:relative}
a{color:inherit;text-decoration:none}

.site-header{position:absolute;left:0;top:0;width:1198px;height:73px;background:#fff;box-shadow:0 1px 3px rgba(0,0,0,.12)}
.brand{position:absolute;left:152px;top:14px;font-family:"Roboto",sans-serif}
.brand-name{display:flex;align-items:center;gap:8px;font-size:20px;font-weight:400;color:var(--navy);letter-spacing:.5px}
.brand-mark{width:14px;height:14px;background:var(--orange)}
.brand-url{font-size:8px;letter-spacing:5px;color:var(--navy);margin-top:4px;padding-left:16px}
.social-top{position:absolute;left:939px;top:23px;display:flex;gap:4px}
.social-top span{width:24px;height:24px;background:#3a3a3a;border-radius:2px;box-shadow:1px 1px 2px rgba(0,0,0,.3)}

.main-nav{position:absolute;left:150px;top:74px;width:898px;height:38px;background:var(--nav);display:flex;align-items:center;justify-content:space-between;padding:0 26px 0 25px;font-family:"Roboto",sans-serif;font-weight:300;font-size:11px;color:#e6e6e6;overflow:hidden}
.main-nav a{white-space:nowrap}
.main-nav a.active{color:var(--orange)}
.dropdown{position:absolute;left:232px;top:112px;width:116px;background:#333;font-family:"Roboto",sans-serif;font-size:10px;color:#9a9a9a}
.dropdown a{display:block;height:25px;line-height:25px;padding-left:9px;border-bottom:1px solid #3f3f3f}
.dropdown a.current{background:#262626;color:#fff}

.hero{position:absolute;left:150px;top:128px;width:650px;height:332px;background:linear-gradient(135deg,#cfd3d6 0%,#f1f1f1 45%,#d8dadc 100%)}
.hero-caption{position:absolute;left:0;top:173px;width:379px;height:100px;background:rgba(25,25,25,.88);color:#fff;padding:18px 25px}
.hero-caption h2{font-family:"Roboto",sans-serif;font-weight:400;font-size:26px;margin-bottom:8px}
.hero-caption p{font-size:11px;line-height:15px;color:#d0d0d0}
.hero-dots{position:absolute;right:16px;bottom:10px;display:flex;gap:4px}
.hero-dots span{width:11px;height:11px;border-radius:50%;background:#333}
.hero-dots span.on{background:#e8e8e8}

.case-list{position:absolute;left:800px;top:128px;width:248px;height:332px;background:var(--panel);padding:14px 18px 0 16px;font-family:"Roboto",sans-serif}
.case-list h3{font-weight:400;font-size:17px;color:#333;padding-bottom:10px;border-bottom:2px solid var(--rule);margin-bottom:14px}
.case-list li{list-style:none;font-size:11.5px;color:#333;height:29px;line-height:28px;border-bottom:1px dashed #bdbdbd;padding-left:15px;position:relative}
.case-list li:last-child{border-bottom:none}
.case-list li::before{content:"›";position:absolute;left:2px;top:0;font-size:14px;color:#555}

.services{position:absolute;left:150px;top:515px;width:898px;display:flex;justify-content:space-between}
.service{width:266px;text-align:center}
.service h3{height:41px;line-height:44px;background:linear-gradient(#fff,#f2f2f2);font-family:"Roboto",sans-serif;font-weight:400;font-size:17px;color:var(--navy)}
.service .photo{height:134px;background:linear-gradient(160deg,#9a9a9a,#4a4a4a 60%,#7d7d7d)}
.service p{font-size:11px;line-height:15.5px;color:#444;margin:16px auto 0;width:225px}
.btn{display:inline-flex;margin-top:17px;height:21px}
.btn .label{background:var(--orange);color:#fff;font-size:13px;line-height:21px;width:63px}
.btn .plus{background:#333;color:#fff;width:20px;line-height:21px;font-size:13px}

.app-band{position:absolute;left:150px;top:858px;width:898px;height:50px;background:#fff;display:flex;align-items:center;justify-content:center;font-family:"Roboto",sans-serif;font-size:17.5px;color:#8c8c8c}
.app-band strong{font-weight:400;color:var(--navy);margin-left:6px}
.app-band svg{margin:0 4px -2px 2px}
.download{background:var(--orange);color:#fff;font-family:"Roboto Condensed",sans-serif;font-size:17px;padding:3px 11px;border:1px solid #c6620f;border-radius:2px}

.site-footer{position:absolute;left:150px;top:908px;width:898px;height:237px;background:var(--dark);color:#e5e5e5}
.site-footer h4{font-family:"Roboto",sans-serif;font-weight:300;font-size:17.5px;color:#d5d5d5;margin-bottom:12px}
.col{position:absolute;top:35px}
.news{left:35px;width:265px}
.news h5{font-size:12px;font-weight:700;margin-bottom:3px}
.news p{font-size:10.5px;line-height:15px}
.news a{display:block;font-size:10.5px;margin:2px 0 14px}
.testimonial{left:341px;width:265px}
.testimonial blockquote{font-style:italic;font-size:10.5px;line-height:15.5px;color:#bdbdbd;margin-top:-1px}
.testimonial cite{display:block;margin-top:20px;font-weight:700;font-size:12.5px;color:#fff}
.testimonial small{display:block;font-style:italic;font-size:10.5px;color:#aaa}
.contact{left:634px;width:240px}
.contact dl{display:grid;grid-template-columns:55px 1fr;row-gap:4px;font-size:10.5px;line-height:15px}
.contact dt{font-family:"Roboto",sans-serif;font-size:12.5px;color:#ccc}
.contact dd.phone{font-weight:700;font-size:12px}
.contact .socials{display:flex;gap:5px;align-items:center;padding-top:3px}
.contact .socials span{width:9px;height:9px;background:#ddd}
.copyright{position:absolute;left:0;top:1168px;width:1198px;text-align:center;font-size:10px;color:#333}
</style>
</head>
<body>
<header class="site-header">
  <a class="brand" href="#">
    <div class="brand-name">HARROW <span class="brand-mark"></span> LINDQVIST</div>
    <div class="brand-url">www.kelbrook.com.au</div>
  </a>
  <div class="social-top" aria-label="Social links"><span></span><span></span><span></span><span></span></div>
</header>

<nav class="main-nav">
  <a href="#">HOME</a>
  <a class="active" href="#">SERVICES +</a>
  <a href="#">CASE STUDIES +</a>
  <a href="#">ENGAGING US</a>
  <a href="#">ABOUT CONFLICT &amp; LOW PERFORMANCE</a>
  <a href="#">CONFLICT RESOLUTION APP</a>
  <a href="#">ABOUT</a>
  <a href="#">CONTACT</a>
</nav>

<section class="hero" role="img" aria-label="Photo of business people working at a desk with laptop and charts">
  <div class="hero-caption">
    <h2>Resolve</h2>
    <p>Aliquam bibendum pretium metus vel ornare. Sed lacinia vulputate dolor, nec congue nunc accumsan at. Praesent leo magna,</p>
  </div>
  <div class="hero-dots"><span></span><span></span><span class="on"></span></div>
</section>

<div class="dropdown">
  <a href="#">SERVICES 1</a>
  <a class="current" href="#">SERVICES 2</a>
  <a href="#">SERVICES 3</a>
</div>

<aside class="case-list">
  <h3>CASE STUDIES</h3>
  <ul>
    <li>Lorem ipsum dolor sit amet,</li>
    <li>Consectetur adipiscing elit. Sed id</li>
    <li>Tempus enim. Etiam eros velit,</li>
    <li>Rutrum in fringilla id, fermentum sit</li>
    <li>Amet nulla. Nullam cursus mi ut</li>
    <li>Lorem commodo eu pharetra elit</li>
    <li>Blandit. Phasellus malesuada,</li>
    <li>Massa et adipiscing</li>
  </ul>
</aside>

<section class="services">
  <article class="service">
    <h3>Assess</h3>
    <div class="photo" role="img" aria-label="Black and white photo of a presenter in a meeting room"></div>
    <p>Aliquam bibendum pretium metus vel ornare. Sed lacinia vulputate dolor, nec congue nunc accumsan at. Praesent leo magna, imperdiet et mollis sed,</p>
    <a class="btn" href="#"><span class="label">Details</span><span class="plus">+</span></a>
  </article>
  <article class="service">
    <h3>Resolve</h3>
    <div class="photo" role="img" aria-label="Black and white photo of colleagues in a boardroom discussion"></div>
    <p>Aliquam bibendum pretium metus vel ornare. Sed lacinia vulputate dolor, nec congue nunc accumsan at. Praesent leo magna, imperdiet et mollis sed,</p>
    <a class="btn" href="#"><span class="label">Details</span><span class="plus">+</span></a>
  </article>
  <article class="service">
    <h3>Develop</h3>
    <div class="photo" role="img" aria-label="Black and white photo of an audience applauding"></div>
    <p>Aliquam bibendum pretium metus vel ornare. Sed lacinia vulputate dolor, nec congue nunc accumsan at. Praesent leo magna, imperdiet et mollis sed,</p>
    <a class="btn" href="#"><span class="label">Details</span><span class="plus">+</span></a>
  </article>
</section>

<div class="app-band">
  Click here to download <strong>Our Conflict Resolution App</strong>
  <svg width="40" height="22" viewBox="0 0 40 22" aria-hidden="true"><path d="M2 18 C6 4,22 0,30 10" fill="none" stroke="#333" stroke-width="1.3"/><path d="M24 10 L31 11 L32 4" fill="none" stroke="#333" stroke-width="1.3"/><path d="M30 16 H38" stroke="#333" stroke-width="1.3"/></svg>
  <a class="download" href="#">Download</a>
</div>

<footer class="site-footer">
  <div class="col news">
    <h4>Latest News</h4>
    <h5>Lorem ipsum dolor sit amet,</h5>
    <p>Adipiscing elit. Sed id tempus enim. Etiam eros velit, rutrum in fringilla id...</p>
    <a href="#">read more</a>
    <h5>Fermentum sit amet nulla. Nullam</h5>
    <p>Cursus mi ut lorem commodo eu pharetra elit blandit. Phasellus malesuada...</p>
    <a href="#">read more</a>
  </div>
  <div class="col testimonial">
    <h4>Testimonials</h4>
    <blockquote>Aliquam bibendum pretium metus vel ornare. Sed lacinia vulputate dolor, nec congue nunc accumsan at. Praesent leo magna, imperdiet et mollis sed, hendrerit id nunc. Vestibulum et dolor enim.</blockquote>
    <cite>Phasellus ut libero</cite>
    <small>Nullam hendrerit magna sit amet</small>
  </div>
  <div class="col contact">
    <h4>Contact Us</h4>
    <dl>
      <dt>Address:</dt><dd>Morbi blandit, odio dignissim laoreet bibendum, nibh sapien condimentum lectus,</dd>
      <dt style="margin-top:6px">Phone:</dt><dd class="phone" style="margin-top:6px">000-000-0000</dd>
      <dt>Email:</dt><dd>phasellus@kelbrook.com.au</dd>
      <dt>Social:</dt><dd class="socials"><span></span><span></span><span></span><span></span></dd>
    </dl>
  </div>
</footer>

<p class="copyright">© Copyright Harrow Lindqvist 2013. All Rights Reserved.</p>
</body>
</html>
```